Korvesh Menu

Hi there,
My restaurant called "Korvesh" means Spice in hebrew.
We are middle eastern restaurant that specialist in dips,salads and hot bread baked on the spot and charcoal grilled meat skewers
The restaurant is pretty casual and the atmosphere is nice and customers feels like home.
on www.korvesh.com.au you can see photos of the restaurant and the food.
ill add up the menus that i would like to be design please and the logo that is on the front of the shop is been add up
thank you

Target Market(s)

The regulars of the restaurant is jewish/israelis

Industry/Entity Type

Restaurant

```html
<!DOCTYPE html>
<html lang="en">
<head>
<meta charset="utf-8">
<title>Korvesh – Entrée Menu</title>
<link href="https://fonts.googleapis.com/css2?family=Crimson+Text:wght@400;700&display=swap" rel="stylesheet">
<style>
  :root {
    --wine-light: #a3101a;
    --wine: #7a0810;
    --wine-deep: #3e0306;
    --gold: #f2c14e;
    --gold-soft: #d9a441;
    --gold-dark: #8a5a1c;
    --ivory: #ffffff;
  }
  * { margin: 0; padding: 0; box-sizing: border-box; }
  html, body { width: 850px; height: 1200px; overflow: hidden; }
  body { background: var(--wine-deep); }

  .menu-page {
    position: relative;
    width: 850px;
    height: 1200px;
    overflow: hidden;
    background: radial-gradient(ellipse at 50% 40%, var(--wine-light) 0%, var(--wine) 45%, var(--wine-deep) 100%);
    font-family: "Crimson Text", Georgia, serif;
    color: var(--gold);
    text-align: center;
  }

  .lattice-backdrop {
    position: absolute;
    inset: 120px 110px 110px 110px;
    background: linear-gradient(180deg, rgba(255,170,120,0.06), rgba(255,170,120,0.03));
  }

  .ornamental-frame {
    position: absolute;
    inset: 0;
    width: 850px;
    height: 1200px;
  }

  .brand-name {
    position: absolute;
    top: 112px;
    left: 0;
    width: 100%;
    font-size: 54px;
    font-weight: 400;
    line-height: 1;
    color: var(--ivory);
  }

  .page-title {
    position: absolute;
    top: 270px;
    left: 0;
    width: 100%;
    font-size: 29px;
    font-weight: 700;
  }

  .menu-section {
    position: absolute;
    left: 0;
    width: 100%;
    font-weight: 700;
  }
  .section-heading {
    font-size: 20px;
    line-height: 1;
    margin-bottom: 18px;
  }
  .section-note {
    font-size: 15px;
    line-height: 1.4;
    margin-bottom: 20px;
  }
  .dish-list { list-style: none; }
  .dish-list li {
    font-size: 15px;
    line-height: 21px;
  }

  .starters { top: 366px; }
  .hummus { top: 573px; }
  .platter { top: 820px; }
</style>
</head>
<body>
<main class="menu-page">
  <div class="lattice-backdrop" role="img" aria-label="Faint interlaced lattice pattern behind the menu text"></div>

  <svg class="ornamental-frame" viewBox="0 0 850 1200" role="img" aria-label="Gold filigree scroll border framing the page">
    <defs>
      <linearGradient id="frameGold" x1="0" y1="0" x2="1" y2="1">
        <stop offset="0" stop-color="#d9a441" stop-opacity="0.75"/>
        <stop offset="0.5" stop-color="#8a5a1c" stop-opacity="0.65"/>
        <stop offset="1" stop-color="#d9a441" stop-opacity="0.75"/>
      </linearGradient>
    </defs>
    <path fill="url(#frameGold)" fill-rule="evenodd"
      d="M0 0H850V1200H0Z M105 70H745V1110H105Z"/>
  </svg>

  <h1 class="brand-name">Korvesh</h1>

  <h2 class="page-title">Entrée</h2>

  <section class="menu-section starters">
    <h3 class="section-heading">Starters</h3>
    <ul class="dish-list">
      <li>6 Falafel Balls On Tahini $5.00</li>
      <li>Moroccan Beef Cigars (3 per serve) $10.00</li>
      <li>Fried Cauliflower $8.00</li>
      <li>Pan Fried Mushrooms and Onions $8.00</li>
      <li>Lamb Kibbeh &amp; Pinenuts (3 per serve) $7.50</li>
    </ul>
  </section>

  <section class="menu-section hummus">
    <h3 class="section-heading">Traditional Hummus</h3>
    <p class="section-note">Served with 1 Laffa and Mixed Pickles</p>
    <ul class="dish-list">
      <li>Masabacha – served with Tahini and whole Chickpeas $11.90</li>
      <li>Ful – served with warm, crushed Fava Beans $14.90</li>
      <li>Mushroom – served with Pan Fried Mushrooms $14.90</li>
      <li>Basar – served with Mince Lamb &amp; Pine nuts $16.50</li>
    </ul>
  </section>

  <section class="menu-section platter">
    <h3 class="section-heading">Salads &amp; Dips Platter</h3>
    <p class="section-note">3 Choices &amp; Laffa for $15.00 or 6 choices &amp; 2 Laffa for $25.00</p>
    <ul class="dish-list">
      <li>Hummus</li>
      <li>Tahini</li>
      <li>Baba Ganoush</li>
      <li>White Cabbage</li>
      <li>Chatzilim (Fried Eggplant)</li>
      <li>Liora’s Corn Salad</li>
      <li>Moroccan Carrot</li>
      <li>Roasted Beetroot</li>
      <li>Turkish Dip</li>
    </ul>
  </section>
</main>
</body>
</html>
```